Plakate für eine Selbstverteidigungs- und Selbstbehauptungsschule
Zielgruppe
Wir sind eine Selbstverteidigungs- und Selbstbehauptungsschule (Krav-Maga) in Hessen (Darmstadt und Rödermark). Wir haben uns darauf spezialisiert, den Menschen zu helfen ihre verschütteten Verteidigungsinstinkte wieder zu entdecken. So wie eine Katze sich von Natur aus verteidigen kann so ist es auch bei uns Menschen. Nur wurde dies uns im Laufe unserer Erziehung und Schulbildung aberzogen. Wir geben den Menschen ihre natürliche Selbstsicherheit zurück. Das sollte so auch deutlich aus der Werbung hervorgehen und auf die Lesenden überspringen.
Zielgruppe sind Menschen, die mit ihrem Selbstbewusstsein hadern (Schüchternheit, Unsicherheit) oder die ihr Selbstvertrauen noch weiter ausbauen wollen. In dieser Werbekampagne geht erstmal nur um Erwachsene.
Der von uns angebotene Kurs heißt: Felsa-Runo-Klar (Pure bedeutet, dass wir Selbstverteidigungstechniken vermitteln, die in leicht zu erlernen und demzufolge in etwaigen Notsituationen auch intuitiv/leicht anzuwenden sind).
Aufgabenstellung
Ich brauche eine neue, ansprechende Werbekampagne für Plakate/Social Media/Flyer, die auf die Wichtigkeit des Themas eingeht und seriös rüberkommt. Wir sind nicht die 'Türsteher' oder 'Schwarz-Gekleideten', sondern eine seriöse Kampfsportschule, die aus eigenen Erfahrungen heraus und mit Leidenschaft unterrichtet. Daher soll die Werbung hochwertig, zielgruppenorientiert und themenfokussiert sein - ähnlich wie bei Autowerbung oder Kosmetik. Sie können sich das so vorstellen, dass wir Selbstvertrauen verkaufen - daher sollte der Fokus darauf liegen, und nicht auf dem Kurs/Sportangebot als solches.
Eine Idee, um das Thema Selbstvertrauen stärker hervorzuheben und auf die Deutlichkeit der angeborenen Verteidigungsinstinkte einzugehen, ist das Aufgreifen unserer Tier-Symbolik auf der Webseite unter https://www.felsa-runo-halt.de/felsa-runo-klar Gerne aber auch eigene Ideen einbringen.
Text Ideen von mir vorab, um Ihnen meine gewünschte Richtung zu verdeutlichen:
- Wecke die Löwin in dir!
- Wecke den Tiger in dir!
- Wecke deine Stärke!
- Stärke dein Selbst!
- Wecke deine Kräfte!
- Werde dein eigener Bodyguard! u.s.w.
Türkis
C:80 M:2 Y:24 K:0
R:0 G:172 B:195
Hex color #00ACC3
gray solid color background:
C:0 M:0 Y:0 K:72,35
R:71 G:71 B:71
Hex color #474747
gray color for white background version:
C:0 M:0 Y:0 K:58
R:140 G:140 B:139
Hex color #8c8c8b
black:
C:91,25 M:78,76 Y:61,98 K:97,47
R:0 G:0 B:0
Hex color #000000
white:
C:0 M:0 Y:0 K:0
R:255 G:255 B:255
Hex color #ffffff
Kind regards
Weitere Logos und Schrifttypen kann ich noch zur Verfügung stellen.
Die Entwürfe müssen in einem Format sein, sodass wir sie später selbst bearbeiten oder anpassen können.

```html
<!DOCTYPE html>
<html lang="de">
<head>
<meta charset="utf-8">
<title>Wecke den Tiger in dir – Plakat</title>
<link href="https://fonts.googleapis.com/css2?family=Anton&family=Oswald:wght@400;500;600&family=Montserrat:wght@500;700&display=swap" rel="stylesheet">
<style>
  :root{
    --orange:#e65114;
    --ink:#333333;
    --paper:#f7f7f7;
    --stage:#e9e9e9;
    --photo-a:#e4e4e4;
    --photo-b:#cfd3d8;
    --icon:#dadada;
  }
  *{margin:0;padding:0;box-sizing:border-box}
  html,body{width:1200px;height:1200px;overflow:hidden;background:var(--stage)}
  .poster{position:absolute;left:0;top:200px;width:1200px;height:800px;background:var(--paper);overflow:hidden;font-family:'Oswald',sans-serif;color:var(--ink)}
  .brand-tab{position:absolute;left:100px;top:0;width:190px;height:233px;background:var(--orange);border-radius:0 0 95px 95px;display:flex;align-items:center;justify-content:center;flex-direction:column;gap:10px}
  .brand-mark{width:14px;height:14px;border-radius:50%;background:#fff}
  .brand-name{font-family:'Oswald',sans-serif;font-weight:600;color:#fff;font-size:19px;letter-spacing:1px;text-transform:uppercase;text-align:center;line-height:1.1}
  .headline{position:absolute;left:60px;top:255px;width:270px;text-align:center;font-family:'Anton',sans-serif;text-transform:uppercase}
  .headline .big{display:block;color:var(--orange);line-height:1}
  .hl-wecke{font-size:94px}
  .hl-tiger{font-size:104px;margin-top:6px}
  .hl-dir{font-size:150px;margin-top:8px}
  .headline .small{display:flex;align-items:center;justify-content:center;gap:14px;color:var(--ink);font-size:36px;line-height:1;margin-top:10px}
  .headline .small::before,.headline .small::after{content:"";height:5px;background:var(--ink);flex:1;max-width:60px}
  .photo{position:absolute;left:315px;top:38px;width:455px;height:684px;background:linear-gradient(160deg,var(--photo-a),var(--photo-b));border-radius:4px}
  .info-box{position:absolute;left:782px;top:79px;width:347px;height:194px;border:2px solid var(--ink);border-radius:18px;padding:28px 18px 0;text-align:center;font-size:21px;font-weight:500;line-height:1.42;text-transform:uppercase}
  .info-title{position:absolute;left:50%;top:-26px;transform:translateX(-50%);background:var(--paper);padding:0 8px;white-space:nowrap;font-size:37px;font-weight:600;line-height:1.2}
  .benefits{position:absolute;left:764px;top:298px;width:370px;display:grid;grid-template-columns:1fr 1fr;row-gap:26px}
  .benefit{text-align:center;text-transform:uppercase;font-weight:500}
  .benefit-icon{width:72px;height:72px;margin:0 auto 12px;background:var(--icon);border-radius:14px}
  .benefit-label{font-size:20px;line-height:1.25}
  .benefit-label.small{font-size:17px}
  .cta{position:absolute;left:708px;top:638px;display:flex;align-items:center;gap:12px}
  .cta-label{font-size:34px;font-weight:600;text-transform:uppercase}
  .cta-phone{background:var(--orange);color:#fff;border-radius:28px;padding:4px 20px;font-size:36px;font-weight:500;white-space:nowrap}
  .social{position:absolute;left:684px;top:713px;width:470px;display:flex;align-items:center;justify-content:flex-end;gap:12px;font-family:'Montserrat',sans-serif}
  .social-dot{width:26px;height:26px;border-radius:50%;background:var(--ink)}
  .social-handle{font-size:13px;font-weight:500;color:var(--ink)}
  .social-url{font-size:15px;font-weight:700;color:var(--orange)}
</style>
</head>
<body>
<main class="poster">
  <div class="brand-tab">
    <span class="brand-mark"></span>
    <span class="brand-name">Felsa-Runo-Klar</span>
  </div>

  <h1 class="headline">
    <span class="big hl-wecke">Wecke</span>
    <span class="small">den</span>
    <span class="big hl-tiger">Tiger</span>
    <span class="small">in</span>
    <span class="big hl-dir">Dir!</span>
  </h1>

  <div class="photo" role="img" aria-label="Foto: Frau wehrt einen Angreifer ab, dahinter ein blasser, brüllender Tiger als Hintergrundgrafik"></div>

  <section class="info-box">
    <h2 class="info-title">Lerne Krav Maga</h2>
    <p>Werden Sie fitter, stärker und lernen Sie eine praktische Selbstverteidigung in einer unterhaltsamen und sicheren Umgebung</p>
  </section>

  <section class="benefits">
    <div class="benefit">
      <div class="benefit-icon" role="img" aria-label="Strichsymbol: strahlende Person"></div>
      <p class="benefit-label">Vertrauen<br>steigern</p>
    </div>
    <div class="benefit">
      <div class="benefit-icon" role="img" aria-label="Strichsymbol: Bizeps mit Herz"></div>
      <p class="benefit-label">Kondition<br>verbessern</p>
    </div>
    <div class="benefit">
      <div class="benefit-icon" role="img" aria-label="Strichsymbol: Herz mit verschränkten Armen"></div>
      <p class="benefit-label small">Lernen Sie eine<br>effektive<br>Selbstverteidigung</p>
    </div>
    <div class="benefit">
      <div class="benefit-icon" role="img" aria-label="Strichsymbol: entspannte Person"></div>
      <p class="benefit-label small">Reduzieren Sie<br>Ihren Stress und<br>Ihre Anspannung</p>
    </div>
  </section>

  <div class="cta">
    <span class="cta-label">Jetzt Call</span>
    <span class="cta-phone">+49 1520 4471935</span>
  </div>

  <div class="social">
    <span class="social-dot"></span>
    <span class="social-handle">@FELSA-RUNO-HALT</span>
    <span class="social-url">www.felsa-runo-halt.de</span>
  </div>
</main>
</body>
</html>
```